Commercial Piping Company Needs A Modern Business Card

We need a clean business card for our commercial pipe lining company. We would like to see a mock up in two color schemes: Black, Grey and Blue and Black, Grey and Orange. We are in the piping industry, but want a professional, clean and modern look to the card.

Industry/Entity Type

Plumbing

Contact Information for Business Card

Name: Mark Telford
Title: Managing Partner
Phone: 608.352.9174
Email: Mark@VeltaSpan.Net

Requirements
Must have
• Back Side Should Have a White Back Ground with Full Logo. Front I would like to see a couple lay outs for contact info. Also the final card will have rounded edges, so please take that into account for printing.
Nice to have
• Two Color Palette Examples
Should not have
• No need for an address line

```html
<!DOCTYPE html>
<html lang="en">
<head>
<meta charset="utf-8">
<title>VeltaSpan Business Card</title>
<link rel="stylesheet" href="https://fonts.googleapis.com/css2?family=Montserrat:wght@400;500;700&display=swap">
<style>
  :root {
    --bg: #e4e5e8;
    --card: #ffffff;
    --ink: #121214;
    --ink-soft: #2a2a2e;
    --accent: #f28a1e;
    --faint: #e6e6e8;
  }
  * { box-sizing: border-box; margin: 0; padding: 0; }
  html, body { width: 1200px; height: 864px; overflow: hidden; }
  body {
    background: var(--bg);
    font-family: "Montserrat", Arial, sans-serif;
    color: var(--ink);
    position: relative;
  }
  .card {
    position: absolute;
    width: 540px;
    height: 309px;
    background: var(--card);
    border-radius: 22px;
    box-shadow: 0 8px 24px rgba(0,0,0,0.12);
    overflow: hidden;
  }
  .card--back { left: 70px; top: 90px; }
  .card--front { left: 590px; top: 460px; }

  .brand { position: absolute; display: flex; align-items: center; gap: 10px; }
  .brand__dot { width: 46px; height: 46px; border-radius: 50%; background: var(--ink); flex: none; }
  .brand__name { font-weight: 500; font-size: 31px; letter-spacing: 1px; line-height: 1; }
  .brand__tag { font-size: 9.5px; letter-spacing: 0.6px; line-height: 1.25; margin-top: 3px; color: var(--ink-soft); }
  .card--back .brand { left: 50%; top: 50%; transform: translate(-50%, -50%); }
  .card--front .brand { left: 32px; top: 48px; }

  .person { position: absolute; right: 30px; top: 30px; text-align: left; }
  .person__name { font-size: 22px; font-weight: 500; letter-spacing: 0.5px; }
  .person__name b { font-weight: 700; }
  .person__title { font-size: 10px; color: var(--accent); letter-spacing: 0.6px; margin-top: 2px; }

  .decor { position: absolute; right: -30px; top: 80px; width: 210px; height: 210px; border-radius: 50%; background: var(--faint); }

  .contact { position: absolute; left: 32px; bottom: 30px; font-size: 12.5px; line-height: 1.55; }
  .contact__label { color: var(--accent); }
</style>
</head>
<body>
  <section class="card card--back" aria-label="Card back">
    <div class="brand">
      <span class="brand__dot"></span>
      <div>
        <div class="brand__name">VELTASPAN</div>
        <div class="brand__tag">PIPE RENEWAL SPECIALISTS<br>INSPECT • DESIGN • RENEW</div>
      </div>
    </div>
  </section>

  <section class="card card--front" aria-label="Card front">
    <div class="decor" aria-hidden="true"></div>
    <div class="brand">
      <span class="brand__dot"></span>
      <div>
        <div class="brand__name">VELTASPAN</div>
        <div class="brand__tag">PIPE RENEWAL SPECIALISTS<br>INSPECT • DESIGN • RENEW</div>
      </div>
    </div>
    <div class="person">
      <div class="person__name"><b>MARK</b> TELFORD</div>
      <div class="person__title">MANAGING PARTNER</div>
    </div>
    <div class="contact">
      <div><span class="contact__label">P</span> : 608.352.9174</div>
      <div><span class="contact__label">E</span> :Mark@VeltaSpan.Net</div>
    </div>
  </section>
</body>
</html>
```